Flyer-Design für Fahrzeugpflege&Lackveredelung
Zielgruppe
Die Firma KM Glanzwerk - Fahrzeugpflege&Lackveredelung ist ein Kleinunternehmen im Car-Detailing Bereich. Hier steht höchste Qualität und maximale Kundenzufriedenheit auf höchster Stelle.
Zielgruppen sind Fahrzeugbesitzer von hochwertigen Wagen, die höchste Ansprüche auf die Fahrzeugaufbereitung legen.
Aber auch das Tagesgeschäft mit Innenraumaufbereitungen für den Normalverbraucher sind möglich.
Aufgabenstellung
Der Flyer soll modern und hochwertig aussehen.
Größe des Flyers: DIN lang (9,8x21)
2-seitig 4/4 farbig
Farben, Daten und Co bitte auf der Internetseite entnehmen
www.kmglanzwerk.de

```html
<!DOCTYPE html>
<html lang="de">
<head>
<meta charset="utf-8">
<title>KM Glanzwerk – Flyer DIN lang</title>
<link href="https://fonts.googleapis.com/css2?family=Raleway:wght@300;400;500;600;700;800&display=swap" rel="stylesheet">
<style>
  :root {
    --canvas: #e8e9eb;
    --paper: #ffffff;
    --ink: #4a4b4d;
    --ink-soft: #5b5c5f;
    --brand-blue: #2f74c0;
    --night: #0b0c0f;
    --night-2: #1c1e24;
    --white: #ffffff;
  }
  * { box-sizing: border-box; margin: 0; padding: 0; }
  html, body { width: 1154px; height: 1200px; overflow: hidden; }
  body {
    background: var(--canvas);
    font-family: "Raleway", Arial, sans-serif;
    color: var(--ink);
    position: relative;
  }
  .page {
    position: absolute;
    top: 29px;
    width: 532px;
    height: 1142px;
    background: var(--paper);
    overflow: hidden;
  }
  .page--front { left: 29px; }
  .page--back { left: 591px; }
  .page-art { position: absolute; inset: 0; width: 100%; height: 100%; }

  /* brand name */
  .brand { position: absolute; text-align: left; }
  .brand__name { font-weight: 500; letter-spacing: -0.5px; line-height: 1; }
  .brand__line { font-weight: 500; line-height: 1.15; }
  .brand--front { left: 338px; top: 70px; color: var(--white); }
  .brand--front .brand__name { font-size: 23px; }
  .brand--front .brand__line { font-size: 13px; letter-spacing: 3px; }
  .brand--front .brand__line + .brand__line { letter-spacing: 1px; padding-left: 18px; }
  .brand--back { left: 376px; top: 50px; color: var(--night); }
  .brand--back .brand__name { font-size: 15px; }
  .brand--back .brand__line { font-size: 8px; letter-spacing: 2px; }
  .brand--back .brand__line + .brand__line { letter-spacing: 0.5px; padding-left: 12px; }

  /* front */
  .headline {
    position: absolute; left: 46px; top: 566px;
    font-weight: 800; font-size: 62px; line-height: 55px;
    letter-spacing: -1.5px; color: var(--ink);
  }
  .headline__accent { color: var(--brand-blue); }
  .service-list { position: absolute; left: 51px; top: 776px; list-style: none; }
  .service-list li {
    display: flex; align-items: center; height: 46.5px;
    font-size: 20px; font-weight: 500; color: var(--ink-soft);
  }
  .service-list svg { width: 28px; height: 22px; margin-right: 14px; flex: none; }
  .service-list .amp { color: var(--brand-blue); }
  .web--front {
    position: absolute; left: 54px; top: 1051px;
    font-size: 15px; font-weight: 500; color: var(--brand-blue);
  }

  /* back */
  .back-title {
    position: absolute; left: 32px; top: 38px;
    font-weight: 800; font-size: 28px; line-height: 26px; letter-spacing: -0.3px;
    color: var(--ink);
  }
  .back-title__accent { color: var(--brand-blue); }
  .service-grid { position: absolute; left: 0; top: 111px; width: 532px; }
  .tile {
    position: absolute; width: 261px; height: 174px;
    display: flex; align-items: center; justify-content: center;
    color: var(--white); font-size: 19px; font-weight: 600;
  }
  .tile span { position: relative; }
  .tile--paint { left: 0; top: 0; background: linear-gradient(135deg,#56585a,#8a8a88 55%,#3e3f41); }
  .tile--coating { left: 271px; top: 0; background: linear-gradient(120deg,#4a4d52,#2a2c31 60%,#7b8088); }
  .tile--interior { left: 0; top: 185px; background: linear-gradient(160deg,#3b3b3b,#1c1c1c 60%,#4a4a4a); }
  .tile--upholstery { left: 271px; top: 185px; background: linear-gradient(90deg,#8d8b86,#a6a39d 50%,#b8b6b0); }
  .tile--leather-clean { left: 0; top: 370px; background: linear-gradient(150deg,#7a7670,#2a2a2c 45%,#3a3a3c); }
  .tile--leather-repair { left: 271px; top: 370px; background: linear-gradient(100deg,#2a2727,#4a4442 45%,#1d1d1f); }

  .more { position: absolute; left: 0; width: 532px; top: 700px; text-align: center; }
  .more__label { font-size: 15px; font-weight: 400; color: var(--ink); line-height: 17px; }
  .more__items { font-size: 13px; font-weight: 700; color: var(--brand-blue); line-height: 16px; }

  .offer { position: absolute; left: 0; width: 532px; top: 748px; text-align: center; }
  .offer__label { font-size: 15px; font-weight: 700; color: var(--ink); }
  .offer__price {
    font-size: 76px; font-weight: 800; color: var(--brand-blue);
    line-height: 72px; letter-spacing: -2px; font-variant-numeric: lining-nums;
    margin-top: 2px;
  }
  .offer__price sup { font-size: 20px; vertical-align: top; position: relative; top: 4px; }
  .offer__price .euro { font-size: 38px; letter-spacing: 0; }
  .offer__note { font-size: 9.5px; line-height: 11.5px; color: var(--ink-soft); margin-top: 3px; }

  .contact { position: absolute; left: 40px; top: 940px; color: var(--white); }
  .contact__owner { font-size: 16px; font-weight: 600; line-height: 24px; }
  .contact__address { font-size: 15px; font-weight: 400; line-height: 20px; margin-top: 6px; }
  .contact__row { display: flex; align-items: center; font-size: 15px; font-weight: 400; height: 29px; }
  .contact__row:first-of-type { margin-top: 4px; }
  .contact__row svg { width: 16px; height: 16px; margin-right: 8px; fill: var(--white); }
  .web--back { font-size: 15px; font-weight: 600; margin-top: 19px; }
</style>
</head>
<body>

<!-- FRONT -->
<section class="page page--front">
  <svg class="page-art" viewBox="0 0 532 1142" preserveAspectRatio="none">
    <defs>
      <linearGradient id="nightFade" x1="0" y1="0" x2="1" y2="1">
        <stop offset="0" stop-color="#16181d"/>
        <stop offset="0.5" stop-color="var(--night)"/>
        <stop offset="1" stop-color="#000"/>
      </linearGradient>
      <linearGradient id="polishTones" x1="0" y1="0" x2="1" y2="1">
        <stop offset="0" stop-color="#5a4638"/>
        <stop offset="0.45" stop-color="#2a211d"/>
        <stop offset="1" stop-color="#0a0a0b"/>
      </linearGradient>
      <radialGradient id="whiteCar" cx="0.7" cy="0.55" r="0.6">
        <stop offset="0" stop-color="#cfd1d4"/>
        <stop offset="0.6" stop-color="#eceded"/>
        <stop offset="1" stop-color="#ffffff"/>
      </radialGradient>
      <linearGradient id="silverCar" x1="0" y1="0" x2="1" y2="0">
        <stop offset="0" stop-color="#6d7078"/>
        <stop offset="1" stop-color="#0b0c0f" stop-opacity="0"/>
      </linearGradient>
    </defs>
    <polygon points="0,0 532,0 532,561 0,320" fill="url(#nightFade)"/>
    <polygon role="img" aria-label="Photo: silver sports car front in a dark studio" points="0,40 150,90 170,260 0,320" fill="url(#silverCar)" opacity="0.7"/>
    <polyline points="52,323 185,283 230,293" fill="none" stroke="#fff" stroke-width="1.2"/>
    <polyline points="52,323 95,340" fill="none" stroke="#fff" stroke-width="1.2"/>
    <polygon points="380,188 529,258 392,508 361,505" fill="var(--brand-blue)"/>
    <polygon role="img" aria-label="Photo: hand polishing a car headlight with a rotary polisher" points="29,393 352,177 504,264 326,552" fill="url(#polishTones)" stroke="#fff" stroke-width="2"/>
    <polyline points="282,478 431,382 499,420 450,505" fill="none" stroke="#fff" stroke-width="1.2"/>
    <polyline points="282,478 365,520" fill="none" stroke="#fff" stroke-width="1.2"/>
    <rect role="img" aria-label="Photo: white sports car front with alloy wheel" x="290" y="800" width="242" height="340" fill="url(#whiteCar)"/>
  </svg>

  <div class="brand brand--front">
    <div class="brand__name">KM Glanzwerk</div>
    <div class="brand__line">Fahrzeugpflege</div>
    <div class="brand__line">Lackveredelung</div>
  </div>

  <h1 class="headline">THE ONLY<br><span class="headline__accent">CAR DETAILER</span><br>YOU NEED.</h1>

  <ul class="service-list">
    <li><svg viewBox="0 0 28 22"><polygon points="0,8 18,0 28,6 20,22" fill="var(--brand-blue)"/></svg>Keramikbeschichtung</li>
    <li><svg viewBox="0 0 28 22"><polygon points="0,8 18,0 28,6 20,22" fill="var(--brand-blue)"/></svg>Lackkorrektur</li>
    <li><svg viewBox="0 0 28 22"><polygon points="0,8 18,0 28,6 20,22" fill="var(--brand-blue)"/></svg>Innenraumaufbereitung</li>
    <li><svg viewBox="0 0 28 22"><polygon points="0,8 18,0 28,6 20,22" fill="var(--brand-blue)"/></svg>Lederpflege&nbsp;<span class="amp">&amp;</span>&nbsp;Reparatur</li>
    <li><svg viewBox="0 0 28 22"><polygon points="0,8 18,0 28,6 20,22" fill="var(--brand-blue)"/></svg>Scheibenversiegelung</li>
  </ul>

  <div class="web--front">www.kmglanzwerk.de</div>
</section>

<!-- BACK -->
<section class="page page--back">
  <svg class="page-art" viewBox="0 0 532 1142" preserveAspectRatio="none">
    <defs>
      <linearGradient id="redCar" x1="0" y1="0" x2="1" y2="1">
        <stop offset="0" stop-color="#ff4a4a"/>
        <stop offset="0.6" stop-color="#d81f26"/>
        <stop offset="1" stop-color="#7a1014"/>
      </linearGradient>
    </defs>
    <polygon points="0,818 532,1090 532,1142 0,1142" fill="var(--brand-blue)"/>
    <polygon points="270,950 532,1083 532,1095 262,958" fill="#4a4b4d"/>
    <polygon role="img" aria-label="Photo: red sports car, front three-quarter view" points="282,925 330,885 420,868 532,866 532,1078 390,1005 290,955" fill="url(#redCar)"/>
  </svg>

  <h2 class="back-title">WAS KANN ICH FÜR<br><span class="back-title__accent">DEIN FAHRZEUG</span> TUN?</h2>

  <div class="brand brand--back">
    <div class="brand__name">KM Glanzwerk</div>
    <div class="brand__line">Fahrzeugpflege</div>
    <div class="brand__line">Lackveredelung</div>
  </div>

  <div class="service-grid">
    <div class="tile tile--paint" role="img" aria-label="Photo: close-up of a paint surface during correction"><span>Lackkorrektur</span></div>
    <div class="tile tile--coating" role="img" aria-label="Photo: coating bottle in front of a dark car"><span>Lackveredelung</span></div>
    <div class="tile tile--interior" role="img" aria-label="Photo: car cockpit and dashboard"><span>Innenraumreinigung</span></div>
    <div class="tile tile--upholstery" role="img" aria-label="Photo: fabric seat before and after cleaning"><span>Polsterreinigung</span></div>
    <div class="tile tile--leather-clean" role="img" aria-label="Photo: black leather sports seat"><span>Lederreinigung</span></div>
    <div class="tile tile--leather-repair" role="img" aria-label="Photo: worn leather seat bolster"><span>Lederreparatur</span></div>
  </div>

  <div class="more">
    <p class="more__label">Weitere Leistungen:</p>
    <p class="more__items">Scheibenversiegelung, Bremsenversiegelung, Wachs-Versiegelung,<br>Cabriodachimprägnierung, Scheinwerferaufbereitung, uvm.</p>
  </div>

  <div class="offer">
    <p class="offer__label">AUSSENAUFBEREITUNG AB</p>
    <p class="offer__price">299<span class="euro">€</span><sup>*</sup></p>
    <p class="offer__note">*Alle Preise orientieren sich an<br>einem gepflegten Fahrzeug<br>im Neuwagenzustand.</p>
  </div>

  <div class="contact">
    <p class="contact__owner">Inh. Kai Mertens</p>
    <p class="contact__address">Talstraße 12<br>34599 Musterfeld</p>
    <p class="contact__row"><svg viewBox="0 0 24 24"><path d="M6.6 10.8a15.1 15.1 0 0 0 6.6 6.6l2.2-2.2c.3-.3.7-.4 1-.2 1.1.4 2.3.6 3.6.6.6 0 1 .4 1 1V20c0 .6-.4 1-1 1C10.6 21 3 13.4 3 4c0-.6.4-1 1-1h3.5c.6 0 1 .4 1 1 0 1.3.2 2.5.6 3.6.1.3 0 .7-.2 1z"/></svg>+49 170 000 1234</p>
    <p class="contact__row"><svg viewBox="0 0 24 24"><path d="M2 5h20v14H2z M3.5 6.5 12 13l8.5-6.5" fill="none" stroke="#fff" stroke-width="2"/><path d="M2 5h20v2l-10 7L2 7z"/></svg>info@kmglanzwerk.de</p>
    <p class="web--back">www.kmglanzwerk.de</p>
  </div>
</section>

</body>
</html>
```